Stationery Design Project

Minimal Design. Black and White Colours Only.
Need Business Card
With Compliments slip
Letterhead
A4 Folder

Target Market(s)

Luxury architectual designed home owners

Industry/Entity Type

Business

Requirements
Must have
• Black and White colours only. Suggest some good textured stock for business card for future printing. try to use font that is used in my logo our some other minimal modern font.

```html
<!DOCTYPE html>
<html lang="en">
<head>
<meta charset="utf-8">
<title>Hale Estates Stationery</title>
<link href="https://fonts.googleapis.com/css2?family=Archivo:wght@600&family=Questrial&display=swap" rel="stylesheet">
<style>
  :root {
    --ink: #111111;
    --paper: #ffffff;
    --backdrop-light: #5e5e5e;
    --backdrop-dark: #3a3a3a;
    --rule: #222222;
  }
  * { margin: 0; padding: 0; box-sizing: border-box; }
  html, body { width: 1024px; height: 1200px; overflow: hidden; }
  body {
    position: relative;
    background: radial-gradient(ellipse at 50% 45%, var(--backdrop-light) 0%, var(--backdrop-dark) 100%);
    font-family: "Questrial", "Century Gothic", sans-serif;
    color: var(--ink);
  }
  .sheet { position: absolute; background: var(--paper); box-shadow: 0 2px 6px rgba(0,0,0,0.25); }
  .brand { position: absolute; display: flex; align-items: center; }
  .brand-square { background: var(--ink); flex: none; }
  .brand-name {
    font-family: "Archivo", "Helvetica Neue", sans-serif;
    font-weight: 600; letter-spacing: -0.01em; white-space: nowrap; line-height: 1;
  }
  .person-name { font-family: "Archivo", "Helvetica Neue", sans-serif; font-weight: 600; }
  .block { position: absolute; line-height: 1.25; white-space: nowrap; }

  /* Compliments slip */
  .slip { left: 192px; top: 112px; width: 606px; height: 315px; }
  .slip .brand { left: 346px; top: 34px; gap: 14px; }
  .slip .brand-square { width: 34px; height: 34px; }
  .slip .brand-name { font-size: 23px; }
  .slip .rule { position: absolute; left: 32px; top: 220px; width: 547px; height: 1.5px; background: var(--rule); }
  .slip .identity { left: 32px; top: 226px; font-size: 8px; }
  .slip .identity .person-name { font-size: 9.5px; }
  .slip .contact { top: 256px; font-size: 8px; }
  .slip .col-phone { left: 32px; }
  .slip .col-address { left: 161px; }
  .slip .col-web { left: 262px; top: 276px; }

  /* Letterhead */
  .letterhead { left: 91px; top: 580px; width: 376px; height: 544px; }
  .letterhead .brand { left: 24px; top: 24px; gap: 9px; }
  .letterhead .brand-square { width: 22px; height: 22px; }
  .letterhead .brand-name { font-size: 14px; }
  .letterhead .details { left: 286px; top: 24px; font-size: 4.6px; line-height: 1.3; }
  .letterhead .details .person-name { font-size: 5.2px; }
  .letterhead .details .gap { height: 5px; }
  .letterhead .footer-web { left: 0; width: 100%; top: 518px; text-align: center; font-size: 5px; }

  /* Business card */
  .card { left: 532px; top: 692px; width: 412px; height: 261px; }
  .card .brand { left: 42px; top: 38px; gap: 13px; }
  .card .brand-square { width: 30px; height: 30px; }
  .card .brand-name { font-size: 19px; }
  .card .identity { left: 44px; top: 111px; font-size: 12px; }
  .card .identity .person-name { font-size: 14px; }
  .card .contact { top: 158px; font-size: 12px; }
  .card .col-phone { left: 44px; }
  .card .col-address { left: 250px; }
  .card .card-web { left: 0; width: 100%; top: 211px; text-align: center; font-size: 12px; }
</style>
</head>
<body>

  <section class="sheet slip" aria-label="Compliments slip">
    <div class="brand">
      <span class="brand-square"></span>
      <span class="brand-name">HALE ESTATES</span>
    </div>
    <div class="rule"></div>
    <div class="block identity">
      <div class="person-name">Marcus Hale</div>
      <div>Managing Director</div>
    </div>
    <div class="block contact col-phone">
      <div>M: +61 400 555 218</div>
      <div>P: +61 7 3000 4827</div>
      <div>E: marcus@haleestates.com</div>
    </div>
    <div class="block contact col-address">
      <div>Level 12, 48 Harbour St</div>
      <div>Portside QLD</div>
      <div>4100 Australia</div>
    </div>
    <div class="block contact col-web">haleestates.com</div>
  </section>

  <section class="sheet letterhead" aria-label="Letterhead">
    <div class="brand">
      <span class="brand-square"></span>
      <span class="brand-name">HALE ESTATES</span>
    </div>
    <div class="block details">
      <div class="person-name">Marcus Hale</div>
      <div>Managing Director</div>
      <div class="gap"></div>
      <div>M: +61 400 555 218</div>
      <div>P: +61 7 3000 4827</div>
      <div>E: marcus@haleestates.com</div>
      <div class="gap"></div>
      <div>Level 12, 48 Harbour St</div>
      <div>Portside QLD</div>
      <div>4100 Australia</div>
    </div>
    <div class="block footer-web">haleestates.com</div>
  </section>

  <section class="sheet card" aria-label="Business card">
    <div class="brand">
      <span class="brand-square"></span>
      <span class="brand-name">HALE ESTATES</span>
    </div>
    <div class="block identity">
      <div class="person-name">Marcus Hale</div>
      <div>Managing Director</div>
    </div>
    <div class="block contact col-phone">
      <div>M: +61 400 555 218</div>
      <div>P: +61 7 3000 4827</div>
      <div>E: marcus@haleestates.com</div>
    </div>
    <div class="block contact col-address">
      <div>Level 12, 48 Harbour St</div>
      <div>Portside QLD</div>
      <div>4100 Australia</div>
    </div>
    <div class="block card-web">haleestates.com</div>
  </section>

</body>
</html>
```